We need a business card design for our website qvwtrading.net. The Star Headline is qvwtrading.net, in large lettering.We sell fashion rings of titanium, mirror pollished stainless steel, and related jewelry. Basically quality products competing with the high expense of gold.We have to portray honesty and trust, because thats who I am. I know marketing, but I am weak on colors and layout. 3D Gold curved edge letters are ok. No green and yellow.Black,Red,Purple and White in small amounts.No fancy Lettering.
No Rainbows in printing.
Our goal is selling our products online globally

Kind Regards Maren Tulloch

Fashion

qvwtrading.net
known for our ideal fit rings
email.marentullochptyltd@corvexmail com

```html
<!DOCTYPE html>
<html lang="en">
<head>
<meta charset="utf-8">
<title>qvwtrading.net – Business Card</title>
<link rel="stylesheet" href="https://fonts.googleapis.com/css2?family=Inter:wght@300;600&display=swap">
<style>
  :root {
    --card-bg-top: #fbfbfb;
    --card-bg-bottom: #f1f1f1;
    --brand-light: #a7a7a9;
    --brand-dark: #3a3a3c;
    --tagline: #3d3d3f;
    --gold: #d6b24a;
    --gold-deep: #a8832a;
    --silver: #d9dbde;
    --silver-deep: #9ea1a6;
    --onyx: #2c2c2e;
  }
  * { margin: 0; padding: 0; box-sizing: border-box; }
  html, body {
    width: 1200px;
    height: 741px;
    overflow: hidden;
  }
  body { font-family: "Inter", "Helvetica Neue", Arial, sans-serif; }

  .card {
    position: relative;
    width: 1200px;
    height: 741px;
    background: linear-gradient(180deg, var(--card-bg-top) 0%, var(--card-bg-bottom) 100%);
    overflow: hidden;
  }

  .brand-block {
    position: absolute;
    top: 108px;
    left: 0;
    width: 1200px;
    display: flex;
    justify-content: center;
  }
  .brand-lockup {
    display: inline-flex;
    flex-direction: column;
    align-items: flex-end;
  }
  .brand-name {
    font-size: 95px;
    font-weight: 600;
    letter-spacing: -3px;
    line-height: 1;
    color: var(--brand-dark);
  }
  .brand-name .brand-prefix { color: var(--brand-light); }

  .tagline {
    margin-top: 14px;
    margin-right: 2px;
    font-size: 30px;
    font-weight: 300;
    letter-spacing: -0.3px;
    color: var(--tagline);
  }

  .ring-row {
    position: absolute;
    top: 338px;
    left: 0;
    width: 1200px;
    height: 300px;
  }
  .ring-photo {
    position: absolute;
    top: 0;
    width: 186px;
    height: 300px;
    border-radius: 90px 90px 60px 60px;
    -webkit-mask-image: linear-gradient(180deg, #000 0%, #000 68%, transparent 100%);
            mask-image: linear-gradient(180deg, #000 0%, #000 68%, transparent 100%);
  }
  .ring-gold-screw   { left: 132px; background: linear-gradient(160deg, var(--gold) 0%, var(--gold-deep) 45%, var(--silver) 75%, var(--silver-deep) 100%); }
  .ring-gold-gem     { left: 380px; background: linear-gradient(160deg, var(--gold) 0%, var(--silver) 50%, var(--silver-deep) 100%); }
  .ring-silver-gem   { left: 636px; background: linear-gradient(160deg, var(--silver) 0%, var(--silver-deep) 55%, var(--silver) 100%); }
  .ring-black-screw  { left: 886px; background: linear-gradient(160deg, var(--onyx) 0%, var(--silver-deep) 55%, var(--silver) 100%); }
</style>
</head>
<body>
  <main class="card">
    <header class="brand-block">
      <div class="brand-lockup">
        <h1 class="brand-name"><span class="brand-prefix">qvw</span>trading.net</h1>
        <p class="tagline">Known for our ideal fit rings</p>
      </div>
    </header>

    <section class="ring-row">
      <div class="ring-photo ring-gold-screw" role="img" aria-label="Photo of a gold and steel band ring with screw details and its reflection"></div>
      <div class="ring-photo ring-gold-gem" role="img" aria-label="Photo of a gold-centred steel band ring set with small stones and its reflection"></div>
      <div class="ring-photo ring-silver-gem" role="img" aria-label="Photo of a polished steel ring with a thin gold stripe and a square-set stone and its reflection"></div>
      <div class="ring-photo ring-black-screw" role="img" aria-label="Photo of a black and steel band ring with screw details and its reflection"></div>
    </section>
  </main>
</body>
</html>
```